Personal letterhead and stationary

I am looking for someone to design letterhead and stationary set for my personal use. I want something simple and timeless with a little bit of color. I like photography, computers and writing.

```html
<!DOCTYPE html>
<html lang="en">
<head>
<meta charset="utf-8">
<title>Mara Quell – 1/3 A4 Envelope</title>
<link rel="stylesheet" href="https://fonts.googleapis.com/css2?family=Source+Sans+3:wght@400;700&display=swap">
<style>
  :root {
    --paper: #ffffff;
    --ink: #000000;
    --envelope-back: #231f20;
    --orange-light: #f7973a;
    --orange-dark: #cb6428;
    --window: #a7a9ac;
    --mark: #231f20;
    --caption: #2b2b2b;
    --white: #ffffff;
  }
  html, body {
    margin: 0;
    padding: 0;
    overflow: hidden;
    background: var(--paper);
  }
  .sheet {
    display: block;
    width: 900px;
    height: 1200px;
    font-family: "Source Sans 3", "Myriad Pro", sans-serif;
  }
  .crop-mark line, .crop-mark circle {
    stroke: var(--mark);
    stroke-width: 1;
    fill: none;
  }
  .flap-band-light { fill: var(--orange-light); }
  .flap-band-dark { fill: var(--orange-dark); }
  .flap-base { fill: var(--ink); }
  .envelope-face { fill: var(--envelope-back); }
  .address-window { fill: var(--window); }
  .brand-dot { fill: var(--orange-dark); }
  .brand-name {
    fill: var(--white);
    font-weight: 700;
    font-size: 25px;
    letter-spacing: 0.5px;
  }
  .sheet-caption {
    fill: var(--caption);
    font-size: 29px;
    font-weight: 400;
  }
  .web-address {
    fill: var(--white);
    font-size: 32px;
    font-weight: 400;
  }
</style>
</head>
<body>
<svg class="sheet" viewBox="0 0 900 1200" xmlns="http://www.w3.org/2000/svg">
  <!-- Envelope flap -->
  <g class="envelope-flap">
    <path class="flap-band-light" d="M35,200 C120,330 400,410 865,415 L865,452 L35,452 Z"/>
    <path class="flap-band-dark" d="M35,208 C125,340 400,418 865,424 L865,452 L35,452 Z"/>
    <path class="flap-base" d="M35,216 C130,352 400,432 865,438 L865,452 L35,452 Z"/>
    <g class="brand">
      <circle class="brand-dot" cx="82" cy="376" r="24"/>
      <text class="brand-name" x="116" y="404">Mara Quell</text>
    </g>
  </g>

  <text class="sheet-caption" x="450" y="497" text-anchor="middle">1/3 A4 Size Envelope</text>

  <!-- Envelope front -->
  <g class="envelope-front">
    <rect class="envelope-face" x="35" y="545" width="830" height="418"/>
    <g class="brand">
      <circle class="brand-dot" cx="106" cy="612" r="24"/>
      <text class="brand-name" x="142" y="640">Mara Quell</text>
    </g>
    <rect class="address-window" x="287" y="687" width="327" height="135" rx="9"/>
    <text class="web-address" x="770" y="943" text-anchor="end">www.maraquell.net</text>
  </g>

  <!-- Crop marks -->
  <g class="crop-mark">
    <circle cx="35" cy="30" r="13"/><line x1="0" y1="30" x2="75" y2="30"/><line x1="35" y1="0" x2="35" y2="70"/>
    <circle cx="865" cy="30" r="13"/><line x1="825" y1="30" x2="900" y2="30"/><line x1="865" y1="0" x2="865" y2="70"/>
    <circle cx="35" cy="452" r="13"/><line x1="0" y1="452" x2="75" y2="452"/><line x1="35" y1="412" x2="35" y2="490"/>
    <circle cx="865" cy="452" r="13"/><line x1="825" y1="452" x2="900" y2="452"/><line x1="865" y1="412" x2="865" y2="490"/>
    <circle cx="35" cy="545" r="13"/><line x1="0" y1="545" x2="75" y2="545"/><line x1="35" y1="507" x2="35" y2="585"/>
    <circle cx="865" cy="545" r="13"/><line x1="825" y1="545" x2="900" y2="545"/><line x1="865" y1="507" x2="865" y2="585"/>
    <circle cx="35" cy="963" r="13"/><line x1="0" y1="963" x2="75" y2="963"/><line x1="35" y1="923" x2="35" y2="1000"/>
    <circle cx="865" cy="963" r="13"/><line x1="825" y1="963" x2="900" y2="963"/><line x1="865" y1="923" x2="865" y2="1000"/>
  </g>
</svg>
</body>
</html>
```